Web Design Project for a Contact Center

We are a contact center catered mainly to Spain and Latin America. We currently have a web site, but the design is very poor. The site is www.vantelinkhub.com.

We would like to have something that works on a content manager, so we can maintain the page. Currently we work with SiteDesk, but it could be any other.

Please see the logos attached

Target Market(s)

Companies and business that may use the services of an outsource contact center

Industry/Entity Type

Google

```html
<!DOCTYPE html>
<html lang="es">
<head>
<meta charset="utf-8">
<title>VanteLink Contact Solutions</title>
<link href="https://fonts.googleapis.com/css2?family=Fira+Sans:wght@300;400;500;600&display=swap" rel="stylesheet">
<style>
  :root{
    --page-bg:#606165;
    --white:#ffffff;
    --panel-bg:#f5f5f5;
    --orange:#f0922e;
    --orange-dark:#d8741a;
    --orange-light:#f7b060;
    --text:#1e1e1e;
    --grey-logo:#6b6c70;
    --divider:#c9c9c9;
    --footer-green:#2d7a10;
  }
  *{box-sizing:border-box;margin:0;padding:0}
  html,body{width:1200px;height:900px;overflow:hidden}
  body{background:var(--page-bg);font-family:"Fira Sans",sans-serif;color:var(--text);position:relative}

  .site-header{position:absolute;left:109px;top:14px;width:987px;height:115px;background:var(--white);border-radius:12px}
  .brand{position:absolute;left:28px;top:30px;display:flex;align-items:center;gap:10px}
  .brand-mark{width:22px;height:22px;background:var(--orange)}
  .brand-name{font-size:40px;font-weight:300;color:var(--grey-logo);letter-spacing:1px;line-height:1}
  .brand-tagline{position:absolute;left:96px;top:81px;font-size:11px;letter-spacing:3px;color:#333;font-weight:500}
  .header-phone{position:absolute;right:66px;top:58px;font-size:21px;font-weight:600;color:var(--orange)}
  .phone-icon{position:absolute;right:20px;top:36px}

  .hero{position:absolute;left:111px;top:137px;width:987px;height:187px;border:2px solid var(--white);
    background:linear-gradient(90deg,#9aa3ae 0%,#c4c3c1 35%,#d9cfc6 60%,#eae4dc 80%,#c7ccd3 100%)}
  .hero-label{position:absolute;left:2px;bottom:6px;width:196px;height:39px;background:rgba(225,225,225,.85);
    font-size:18px;color:#333;padding:8px 0 0 42px}

  .sidebar{position:absolute;left:107px;top:333px;width:221px;height:478px;background:var(--panel-bg);
    border:1px solid #333;border-radius:12px}
  .nav-list{list-style:none;position:absolute;left:8px;top:92px;width:200px}
  .nav-list li{font-size:15px;line-height:19px;padding:10px 0 10px 0;position:relative}
  .nav-list li::after{content:"";position:absolute;left:20px;right:-18px;bottom:0;height:1px;
    background:linear-gradient(90deg,transparent,var(--orange-light) 50%,transparent)}
  .nav-active{position:absolute;left:86px;top:363px;width:252px;height:49px;z-index:2}
  .nav-active-tab{position:absolute;left:0;top:0;width:242px;height:49px;background:linear-gradient(180deg,var(--orange-light),var(--orange-dark));
    box-shadow:0 2px 4px rgba(0,0,0,.35);color:var(--white);font-size:15px;line-height:19px;padding:6px 0 0 30px}

  .content{position:absolute;left:338px;top:332px;width:760px;height:479px;background:var(--panel-bg);
    border:2px solid var(--orange);border-radius:14px}
  .content h1{position:absolute;left:20px;top:16px;font-size:17.5px;font-weight:600;color:var(--orange)}
  .intro{position:absolute;left:21px;top:50px;width:705px;font-size:13.6px;line-height:17.5px}
  .intro p+p{margin-top:17px}
  .btn{position:absolute;display:block;height:27px;border-radius:14px;color:var(--white);font-size:13.5px;text-align:center;
    line-height:27px;background:linear-gradient(180deg,var(--orange-light),var(--orange-dark));box-shadow:0 1px 2px rgba(0,0,0,.3)}
  .btn-read{left:628px;top:205px;width:87px}
  .column{position:absolute;top:245px}
  .column h2{font-size:17.5px;font-weight:600;color:var(--orange);margin-left:8px}
  .col-org{left:26px;width:340px}
  .col-srv{left:438px;width:300px}
  .column ul{list-style:none;margin-top:16px}
  .org-list li{font-size:13.6px;line-height:13.5px;padding-left:20px;position:relative;margin-bottom:12px}
  .org-list li::before{content:"";position:absolute;left:5px;top:4px;width:8px;height:8px;border-radius:50%;background:var(--orange)}
  .srv-list li{font-size:13.6px;line-height:21px;padding-left:20px;position:relative}
  .srv-list li::before{content:"";position:absolute;left:1px;top:6px;width:10px;height:10px;background:linear-gradient(135deg,var(--orange-light),var(--orange-dark))}
  .btn-org{left:34px;top:409px;width:146px}
  .btn-srv{left:438px;top:409px;width:146px}

  .site-footer{position:absolute;left:103px;top:844px;width:990px;height:80px;border-radius:12px;
    background:linear-gradient(180deg,var(--orange-light),var(--orange) 40%);box-shadow:0 0 6px rgba(255,200,140,.6)}
  .footer-links{position:absolute;top:22px;left:0;right:0;text-align:center;font-size:15.5px;color:var(--white)}
  .footer-links span{margin:0 4px}
  .footer-links .powered{color:var(--footer-green);margin-left:10px}
</style>
</head>
<body>
  <header class="site-header">
    <div class="brand"><span class="brand-mark"></span><span class="brand-name">vantelink</span></div>
    <div class="brand-tagline">CONTACT SOLUTIONS</div>
    <div class="header-phone">(+123) 555 - 204 - 61870</div>
    <svg class="phone-icon" width="42" height="40" viewBox="0 0 42 40" aria-hidden="true">
      <ellipse cx="21" cy="18" rx="19" ry="16" fill="#3a9be0"/>
      <path d="M10 32 L8 39 L17 33 Z" fill="#3a9be0"/>
      <path d="M14 10 q-3 3 2 10 q5 6 9 5 l2-3 -4-3 -2 2 q-3-2 -5-6 l2-1 -2-5 z" fill="#fff"/>
    </svg>
  </header>

  <section class="hero" role="img" aria-label="Fotografía de operadores de call center con auriculares trabajando en la oficina">
    <div class="hero-label">Call Solution</div>
  </section>

  <aside class="sidebar">
    <ul class="nav-list">
      <li>Aumente su Rentabilidad<br>Mediante un Contact<br>Center Externo</li>
      <li>Capacidades</li>
      <li>Contacto</li>
      <li>+ La más avanzada tecnología</li>
      <li>Nuestros Clientes</li>
      <li>+ Oportunidades Laborales</li>
      <li>Por Qué Uruguay?</li>
      <li>Sitemap</li>
    </ul>
  </aside>
  <div class="nav-active">
    <svg width="252" height="49" viewBox="0 0 252 49" style="position:absolute;left:0;top:0" aria-hidden="true">
      <polygon points="0,45 14,49 14,40" fill="#b35c10"/>
      <polygon points="242,10 252,14 252,35 242,39" fill="#e07c1e"/>
    </svg>
    <div class="nav-active-tab">Un Call Center Orientado<br>a la Venta</div>
  </div>

  <main class="content">
    <h1>Un Call Center Orientado a la Venta</h1>
    <div class="intro">
      <p>VanteLink es un Contact Center ubicado en Uruguay, y orientado especialmente a actividades de Telemarketing y Televentas.</p>
      <p>VanteLink ha sido fundado por ejecutivos con larga trayectoria y experiencia en ventas y atención a clientes. Pese a su gran crecimiento del último tiempo, VanteLink ha tenido un especial cuidado en la selección de personal, con especial énfasis en los supervisores, quienes son, al final del día, quienes tienen mayor influencia en la calidad de la atención a los clientes y de los resultados de ventas. Somos un equipo de profesionales orientados a prestar un servicio especializado, personalizando a cada cliente, y brindando soluciones inmediatas y eficientes.</p>
    </div>
    <a class="btn btn-read">read more</a>

    <section class="column col-org">
      <h2>Nuestra Organización:</h2>
      <ul class="org-list">
        <li>Software CALLNEXUS (www.callnexussoft.com)</li>
        <li>Supervisión y control de las operaciones en tiempo real, que facilitan la toma de decisiones orientadas a mejorar la productividad y reasignar recursos</li>
        <li>Módulos integrados de marcación y grabación IVR</li>
        <li>Back up capacitado para cubrir ausencias</li>
      </ul>
    </section>
    <section class="column col-srv">
      <h2>Nuestros Servicios:</h2>
      <ul class="srv-list">
        <li>Gestión de ventas</li>
        <li>Productos financieros</li>
        <li>Encuestas y sondeos de mercado</li>
        <li>Gestión de cobranzas</li>
        <li>Gestión de morosos</li>
        <li>Gestión de pedidos de mercadería</li>
      </ul>
    </section>
    <a class="btn btn-org">more organizacions</a>
    <a class="btn btn-srv">more servicios</a>
  </main>

  <footer class="site-footer">
    <div class="footer-links">
      Sign in <span>|</span> Recent Site Activity <span>|</span> Terms <span>|</span> Report Abuse <span>|</span> Print page <span>|</span><span class="powered">Powered by SiteDesk</span>
    </div>
  </footer>
</body>
</html>
```